Flyer design for webdesign company

create a flyer that can be printed or sent as an email. The flyer needs to be professional, modern and engaging.

Project Deadline Extended
Reason: opportunity for all designers to get their designs in.

Target Market(s)

business owners that do not have a website

Industry/Entity Type

It Company

Font styles to use
Sans Serif

```html
<!DOCTYPE html>
<html lang="en">
<head>
<meta charset="utf-8">
<title>Web Design Flyer</title>
<link rel="stylesheet" href="https://fonts.googleapis.com/css2?family=Oswald:wght@500;600&family=Open+Sans:wght@300;400&display=swap">
<style>
  :root {
    --pink: #e0207a;
    --pink-light: #fde0ee;
    --cyan: #1aaee8;
    --orange: #e8892e;
    --grey-text: #4a4a4a;
    --rule: #c9c9c9;
    --paper: #ffffff;
    --backdrop: #ececec;
  }
  * { margin: 0; padding: 0; box-sizing: border-box; }
  html, body { width: 1200px; height: 1200px; overflow: hidden; }
  body { background: var(--backdrop); font-family: "Open Sans", sans-serif; }

  .flyer {
    position: absolute; left: 167px; top: 40px;
    width: 866px; height: 1120px;
    background: var(--paper); overflow: hidden;
  }
  .frame-band { position: absolute; left: 0; top: 0; width: 866px; height: 517px; background: var(--pink); }
  .hero-photo {
    position: absolute; left: 28px; top: 29px; width: 811px; height: 574px;
    background: linear-gradient(160deg, #c99461 0%, #d6a26c 35%, #b97b48 70%, #8a5733 100%);
  }
  .price-badge {
    position: absolute; left: 441px; top: 383px; width: 156px; height: 156px;
    border-radius: 50%; background: var(--orange);
    box-shadow: 0 0 0 6px rgba(255,255,255,0.25);
    display: flex; flex-direction: column; align-items: center; justify-content: center;
    font-family: "Oswald", sans-serif; font-weight: 500; color: #fff;
    font-size: 38px; line-height: 1; letter-spacing: -0.5px;
  }
  .headline-ring {
    position: absolute; left: 39px; top: 538px; width: 364px; height: 364px;
    border-radius: 50%; border: 1.5px solid var(--rule); background: var(--paper);
  }
  .headline-disc {
    position: absolute; left: 53px; top: 552px; width: 336px; height: 336px;
    border-radius: 50%; background: var(--pink); color: var(--pink-light);
    font-family: "Oswald", sans-serif; font-weight: 500; text-align: center;
    display: flex; flex-direction: column; align-items: center; justify-content: center;
    line-height: 0.95; letter-spacing: -1px;
  }
  .headline-disc .small { font-size: 62px; transform: scaleX(0.82); }
  .headline-disc .big { font-size: 146px; font-weight: 600; transform: scaleX(0.82); line-height: 0.9; }

  .tagline {
    position: absolute; left: 411px; top: 614px; width: 400px; text-align: center;
    font-family: "Oswald", sans-serif; font-weight: 500; color: var(--cyan);
    font-size: 34px; line-height: 38px; letter-spacing: -0.5px; white-space: nowrap;
  }
  .tagline span { display: block; transform: scaleX(0.84); transform-origin: center; }
  .brand {
    position: absolute; left: 411px; top: 762px; width: 400px;
    display: flex; align-items: center; justify-content: center; gap: 12px;
  }
  .brand-dot { width: 48px; height: 48px; border-radius: 50%; background: var(--orange); }
  .brand-name { font-size: 32px; font-weight: 400; color: var(--grey-text); line-height: 1; }

  .offer {
    position: absolute; left: 380px; top: 846px; width: 440px; text-align: center;
    font-family: "Oswald", sans-serif; font-weight: 500; color: var(--orange);
    font-size: 44px; line-height: 1; white-space: nowrap;
  }
  .offer small { font-size: 17px; }
  .contact {
    position: absolute; left: 350px; top: 900px; width: 500px; text-align: center;
    font-size: 17px; color: var(--grey-text); white-space: nowrap;
  }

  .features { position: absolute; left: 0; top: 938px; width: 866px; height: 126px; }
  .feature { position: absolute; top: 0; text-align: center; width: 200px; }
  .feature h3 {
    font-family: "Oswald", sans-serif; font-weight: 500; color: var(--pink);
    font-size: 40px; line-height: 38px; letter-spacing: -0.5px;
    transform: scaleX(0.85);
  }
  .feature p { font-size: 15.5px; font-weight: 300; color: var(--grey-text); line-height: 21px; margin-top: 4px; }
  .divider { position: absolute; top: 2px; width: 1.5px; height: 122px; background: var(--rule); }

  .base-rule { position: absolute; left: 0; top: 1075px; width: 866px; height: 2px; background: #dcdcdc; }
  .base-band { position: absolute; left: 0; top: 1081px; width: 866px; height: 39px; background: var(--orange); }
</style>
</head>
<body>
  <div class="flyer">
    <div class="frame-band"></div>
    <div class="hero-photo" role="img" aria-label="Photo of a wooden desk with a computer monitor showing a web design page, a plant, coffee cup, sticky notes, keyboard and a hand on a mouse"></div>

    <div class="price-badge"><span>ONLY $3</span><span>A DAY</span></div>

    <div class="headline-ring"></div>
    <div class="headline-disc">
      <span class="small">ATTRACT</span>
      <span class="big">MORE</span>
      <span class="small">CUSTOMERS</span>
    </div>

    <div class="tagline">
      <span>STOP WASTING MONEY ON MAILERS</span>
      <span>AND PRINT ADVERTISING</span>
    </div>

    <div class="brand">
      <span class="brand-dot"></span>
      <span class="brand-name">novasites</span>
    </div>

    <div class="offer">ONLY $99 / MONTH <small>(NO OTHER COSTS)</small></div>
    <div class="contact">Call today &nbsp;1-800-555-0142 &nbsp;&nbsp;•&nbsp; www.novasites-web.com</div>

    <div class="features">
      <div class="feature" style="left:15px;">
        <h3>97%</h3>
        <p>Of people look online<br>for businesses.<br>You need a website.</p>
      </div>
      <div class="divider" style="left:217px;"></div>
      <div class="feature" style="left:217px;">
        <h3>BEAT</h3>
        <p>your competition<br>with better visibility<br>and credibility</p>
      </div>
      <div class="divider" style="left:415px;"></div>
      <div class="feature" style="left:421px;">
        <h3>SMART</h3>
        <p>clean website designs<br>($3000 value.<br>no extra charge)</p>
      </div>
      <div class="divider" style="left:623px;"></div>
      <div class="feature" style="left:632px;">
        <h3>SOCIAL<br>MEDIA</h3>
        <p>set up options<br>(Search and Social).</p>
      </div>
    </div>

    <div class="base-rule"></div>
    <div class="base-band"></div>
  </div>
</body>
</html>
```